TIPSY PANTRY needs a show poster

"Tipsy Pantry" is a stand up comedy show. We need a fun, eye-catching poster. The taglines are "Heaps of Laughter" and "Fresh Comedy, Shaken Martinis." We are attaching our logo files and a vintage photo that we sometimes use, but they do not need to be a part of the poster. We like vintage* and retro* images but are open to the creativity of the designer.

* Added note: Vintage and Retro to us means 1950s-1970s design types, not distressed and worn looking. Color is good!

Target Market(s)

Women & Couples, Ages 30-70

Industry/Entity Type

Comedy

Requirements
Must have
• Title: Tipsy Pantry
• Primary Tagline: Loads of Laughs
• Performers Names: Helen Forsyth & Joan Pettibrook
Nice to have
• Secondary Tagline: Fresh Comedy, Shaken Martinis.
Should not have
• No cliche images of stand up comedy (spotlight, stage, microphone)

```html
<!DOCTYPE html>
<html lang="en">
<head>
<meta charset="utf-8">
<title>Tipsy Pantry – Show Poster</title>
<link href="https://fonts.googleapis.com/css2?family=Archivo+Black&family=Roboto+Condensed:wght@700&display=swap" rel="stylesheet">
<style>
  :root {
    --stage-bg: #e9e7e4;
    --poster-shadow: rgba(0,0,0,0.18);
    --pattern-magenta: #e8248c;
    --pattern-purple: #7a3fa0;
    --pattern-orange: #f26a1b;
    --pattern-yellow: #f7d417;
    --ink-black: #141414;
    --text-white: #ffffff;
    --band-yellow: #f5ea1c;
    --names-purple: #5b2c8a;
  }
  html, body {
    margin: 0;
    padding: 0;
    width: 1200px;
    height: 797px;
    overflow: hidden;
    background: var(--stage-bg);
  }
  .canvas {
    position: relative;
    width: 1200px;
    height: 797px;
  }
  .poster {
    position: absolute;
    left: 370px;
    top: 28px;
    width: 460px;
    height: 740px;
    overflow: hidden;
    box-shadow: 0 8px 24px var(--poster-shadow);
  }
  .poster__pattern {
    position: absolute;
    left: 0;
    top: 0;
    width: 460px;
    height: 698px;
    display: block;
  }
  .poster__title-disc {
    position: absolute;
    left: 90px;
    top: 110px;
    width: 280px;
    height: 280px;
    border-radius: 50%;
    background: var(--ink-black);
  }
  .poster__title {
    position: absolute;
    left: 0;
    top: 168px;
    width: 460px;
    margin: 0;
    text-align: center;
    font-family: "Archivo Black", sans-serif;
    font-weight: 400;
    font-size: 58px;
    line-height: 62px;
    letter-spacing: -1px;
    color: var(--text-white);
  }
  .poster__taglines {
    position: absolute;
    left: 0;
    top: 378px;
    width: 460px;
    margin: 0;
    padding: 0;
    list-style: none;
    text-align: center;
    font-family: "Archivo Black", sans-serif;
    color: var(--text-white);
    text-shadow:
      2px 0 0 var(--ink-black), -2px 0 0 var(--ink-black),
      0 2px 0 var(--ink-black), 0 -2px 0 var(--ink-black),
      2px 2px 0 var(--ink-black), -2px -2px 0 var(--ink-black),
      2px -2px 0 var(--ink-black), -2px 2px 0 var(--ink-black);
  }
  .tagline--primary {
    font-size: 25px;
    line-height: 36px;
  }
  .tagline--secondary {
    font-size: 21px;
    line-height: 37px;
  }
  .poster__band {
    position: absolute;
    left: 0;
    bottom: 0;
    width: 460px;
    height: 42px;
    background: var(--band-yellow);
    display: flex;
    align-items: center;
    justify-content: center;
  }
  .poster__performers {
    margin: 0;
    font-family: "Roboto Condensed", sans-serif;
    font-weight: 700;
    font-size: 20px;
    color: var(--names-purple);
  }
</style>
</head>
<body>
<main class="canvas">
  <article class="poster">
    <svg class="poster__pattern" role="img" aria-label="Retro pattern of bold overlapping concentric circles in magenta, purple, orange, yellow and black" viewBox="0 0 460 698" preserveAspectRatio="none">
      <defs>
        <linearGradient id="patternTones" x1="0" y1="0" x2="1" y2="1">
          <stop offset="0" stop-color="#e8248c"/>
          <stop offset="0.4" stop-color="#7a3fa0"/>
          <stop offset="0.75" stop-color="#f26a1b"/>
          <stop offset="1" stop-color="#f7d417"/>
        </linearGradient>
      </defs>
      <rect width="460" height="698" fill="url(#patternTones)"/>
    </svg>
    <div class="poster__title-disc"></div>
    <h1 class="poster__title">TIPSY<br>PANTRY</h1>
    <ul class="poster__taglines">
      <li class="tagline--primary">HEAPS OF LAUGHTER</li>
      <li class="tagline--secondary">FRESH COMEDY</li>
      <li class="tagline--secondary">SHAKEN MARTINIS</li>
    </ul>
    <footer class="poster__band">
      <p class="poster__performers">Helen Forsyth &amp; Joan Pettibrook</p>
    </footer>
  </article>
</main>
</body>
</html>
```